PowerPoint template for Credit Card Processor

We need a powerpoint template for our new credit card processing company. Our goal is to sign up merchants to accept credit cards. We will be making presentations to merchants to get them to sign up for our services.

We already have a logo designed. We'd like to incorporate that logo and color scheme in the powerpoint template. The logo file is an illustrator file.

I generally like light colored backgrounds. Nothing too dark.

Industry/Entity Type

Credit Card

Requirements
Must have
• our logo

```html
<!DOCTYPE html>
<html lang="en">
<head>
<meta charset="utf-8">
<title>Services – Presentation Template</title>
<link href="https://fonts.googleapis.com/css2?family=Open+Sans:wght@400&family=Roboto+Condensed:wght@300;400&family=Ubuntu:wght@400;500;700&display=swap" rel="stylesheet">
<style>
:root{
  --blue:#0a86c6;
  --navy:#0c5688;
  --navy-deep:#0a4a7a;
  --teal:#1fa9a6;
  --ink:#4a4f55;
  --grey:#9a9ea3;
  --paper:#f8f9fb;
  --pale:#dff2f9;
}
*{box-sizing:border-box;margin:0;padding:0}
html,body{width:1200px;height:941px;overflow:hidden;background:#fff}
body{position:relative;font-family:"Open Sans",sans-serif;color:var(--ink)}
.slide{position:absolute;overflow:hidden;background:linear-gradient(160deg,var(--paper) 55%,var(--pale) 100%)}
.slide--cover{left:14px;top:58px;width:573px;height:429px;background:linear-gradient(135deg,#0d5f95 0%,var(--navy) 50%,var(--navy-deep) 100%)}
.slide--cards{left:605px;top:58px;width:569px;height:429px}
.slide--mission{left:19px;top:501px;width:565px;height:409px}
.slide--customers{left:613px;top:501px;width:569px;height:409px}

.cover-title{position:absolute;left:0;width:573px;top:170px;text-align:center;font-family:"Roboto Condensed",sans-serif;font-size:40px;color:#fff;font-weight:400}
.brand{position:absolute;display:flex;align-items:center;gap:6px;font-family:"Roboto Condensed",sans-serif;font-weight:300;font-size:17px}
.brand__dot{width:13px;height:13px;border-radius:50%;background:currentColor}
.cover-brand{right:12px;bottom:8px;color:#fff}
.footer-brand{right:10px;bottom:8px;color:var(--grey);font-size:20px}
.footer-brand .brand__dot{width:16px;height:16px}

.headline{position:absolute;display:flex;align-items:center;gap:10px;font-family:"Roboto Condensed",sans-serif;font-size:54px;color:var(--blue);line-height:1}
.headline__dot{width:36px;height:36px;border-radius:50%;background:var(--blue)}
.slide--cards .headline{right:14px;top:12px}

.side-bar{position:absolute;left:0;top:0;width:17px;height:100%;background:var(--blue)}
.page-num{position:absolute;bottom:8px;font-family:"Ubuntu",sans-serif;font-weight:700;font-size:15px;color:var(--blue)}
.side-bar .page-num{left:3px;color:#d8eef8}

.column{position:absolute;top:84px;width:164px}
.title{font-family:"Ubuntu",sans-serif;font-weight:700;font-size:19.5px;color:var(--blue);line-height:1.2;white-space:nowrap}
.subtitle{font-family:"Ubuntu",sans-serif;font-size:12.5px;color:var(--teal);white-space:nowrap;margin-top:4px}
.body{font-size:10.5px;line-height:12.4px;text-align:justify;margin-top:11px;color:var(--ink)}
.photo{position:absolute;top:242px;width:156px;height:156px;border-radius:50%}
.photo--terminal{left:25px;background:radial-gradient(circle at 45% 55%,#5b6f8a,#cfd5de 70%)}
.photo--keyboard{left:208px;background:linear-gradient(150deg,#2a8fc4 0%,#7cc0e2 45%,#e9ecef 70%)}
.photo--stack{left:393px;background:linear-gradient(160deg,#d9413a 0%,#e98c7e 40%,#3b6fb8 70%,#1e4c93 100%)}

.tab{position:absolute;left:0;height:34px;background:var(--blue);color:#fff;font-family:"Roboto Condensed",sans-serif;font-size:20px;line-height:34px;padding-left:26px}
.tab-end{position:absolute;width:16px;height:34px;background:var(--blue)}
.slide--mission .tab{width:266px;top:17px}
.slide--mission .tab-end{left:549px;top:17px}
.slide--mission .headline{left:278px;top:7px;font-size:54px}
.slide--customers .tab{width:270px;top:21px}
.slide--customers .tab-end{left:553px;top:21px}
.slide--customers .headline{left:282px;top:11px;font-size:54px}

.block{position:absolute}
.block .title{font-size:16.5px}
.block .subtitle{font-size:12.5px;margin:0 0 3px}
.note{position:absolute;display:flex;gap:10px;align-items:flex-start}
.note__box{width:88px;height:50px;background:var(--blue);flex:none}
.note__text{width:102px;font-size:6.6px;line-height:7.2px;text-align:justify;margin-top:-1px}
.slide svg{position:absolute;left:0;top:0}
.globe{position:absolute;left:224px;top:157px;width:112px;height:112px;border-radius:50%;background:var(--blue)}
.person{position:absolute;left:252px;top:171px;width:74px;height:74px;border-radius:50%;background:var(--blue)}
</style>
</head>
<body>

<section class="slide slide--cover">
  <h1 class="cover-title">Services</h1>
  <div class="brand cover-brand"><span class="brand__dot"></span>SwiftRelay.net</div>
</section>

<section class="slide slide--cards">
  <div class="side-bar"><span class="page-num">6</span></div>
  <div class="headline"><span class="headline__dot"></span>Services</div>
  <div class="column" style="left:23px">
    <h2 class="title">Title lorem ipsum</h2>
    <p class="subtitle">subtitle ipsum dolor sit amet</p>
    <p class="body">Lorem ipsum dolor sit amet, consectetur adipiscing elit. Vestibulum at suscipit ipsum. Quisque vel turpis justo. Duis porttitor tortor ut dolor sodales, ut ornare augue lacinia. Morbi risus elit, aliquet in purus eget.</p>
  </div>
  <div class="column" style="left:208px">
    <h2 class="title">Title lorem ipsum</h2>
    <p class="subtitle">subtitle ipsum dolor sit amet</p>
    <p class="body">Lorem ipsum dolor sit amet, consectetur adipiscing elit. Vestibulum at suscipit ipsum. Quisque vel turpis justo. Duis porttitor tortor ut dolor sodales, ut ornare augue lacinia. Morbi risus elit, aliquet in purus eget, feugiat auctor urna.</p>
  </div>
  <div class="column" style="left:393px">
    <h2 class="title">Title lorem ipsum</h2>
    <p class="subtitle">subtitle ipsum dolor sit amet</p>
    <p class="body">Lorem ipsum dolor sit amet, consectetur adipiscing elit. Vestibulum at suscipit ipsum. Quisque vel turpis justo. Duis porttitor tortor ut dolor sodales, ut ornare augue lacinia.</p>
  </div>
  <div class="photo photo--terminal" role="img" aria-label="Photo of a card being swiped through a payment terminal"></div>
  <div class="photo photo--keyboard" role="img" aria-label="Photo of a blue credit card resting on a keyboard"></div>
  <div class="photo photo--stack" role="img" aria-label="Photo of a stack of colourful credit cards"></div>
  <div class="brand footer-brand"><span class="brand__dot"></span>SwiftRelay.net</div>
</section>

<section class="slide slide--mission">
  <div class="tab">Our mission</div>
  <div class="headline"><span class="headline__dot"></span>Services</div>
  <div class="tab-end"></div>
  <svg width="565" height="409" aria-hidden="true">
    <g fill="none" stroke="var(--blue)" stroke-width="1.2">
      <polyline points="118,142 216,142 246,174"/>
      <polyline points="288,163 308,114 350,114"/>
      <polyline points="118,269 222,269 244,254"/>
      <polyline points="294,266 306,281 350,281"/>
    </g>
  </svg>
  <div class="globe" role="img" aria-label="Globe icon"></div>
  <div class="block" style="left:352px;top:84px"><p class="subtitle">subtitle ipsum dolor sit amet</p><h2 class="title">Title lorem ipsum</h2></div>
  <div class="block" style="left:15px;top:124px"><p class="subtitle">subtitle ipsum dolor sit amet</p><h2 class="title">Title lorem ipsum</h2></div>
  <div class="block" style="left:16px;top:250px"><p class="subtitle">subtitle ipsum dolor sit amet</p><h2 class="title">Title lorem ipsum</h2></div>
  <div class="block" style="left:345px;top:250px"><p class="subtitle">subtitle ipsum dolor sit amet</p><h2 class="title">Title lorem ipsum</h2></div>
  <div class="note" style="left:351px;top:130px"><span class="note__box"></span><p class="note__text">Lorem ipsum dolor sit amet, consectetur adipiscing elit. Vestibulum at suscipit ipsum. Quisque vel turpis justo. Duis porttitor tortor ut dolor sodales, ut ornare augue lacin-</p></div>
  <div class="note" style="left:16px;top:169px"><span class="note__box"></span><p class="note__text">Lorem ipsum dolor sit amet, consectetur adipiscing elit. Vestibulum at suscipit ipsum. Quisque vel turpis justo. Duis porttitor tortor ut dolor sodales, ut ornare augue lacin-</p></div>
  <div class="note" style="left:16px;top:295px"><span class="note__box"></span><p class="note__text">Lorem ipsum dolor sit amet, consectetur adipiscing elit. Vestibulum at suscipit ipsum. Quisque vel turpis justo. Duis porttitor tortor ut dolor sodales, ut ornare augue lacin-</p></div>
  <div class="note" style="left:344px;top:295px"><span class="note__box"></span><p class="note__text">Lorem ipsum dolor sit amet, consectetur adipiscing elit. Vestibulum at suscipit ipsum. Quisque vel turpis justo. Duis porttitor tortor ut dolor sodales, ut ornare augue lacin-</p></div>
  <span class="page-num" style="left:6px">8</span>
  <div class="brand footer-brand"><span class="brand__dot"></span>SwiftRelay.net</div>
</section>

<section class="slide slide--customers">
  <div class="tab">Customers</div>
  <div class="headline"><span class="headline__dot"></span>Services</div>
  <div class="tab-end"></div>
  <svg width="569" height="409" aria-hidden="true">
    <g stroke="var(--blue)" stroke-width="8" stroke-linecap="round">
      <line x1="289" y1="152" x2="289" y2="136"/>
      <line x1="317" y1="160" x2="325" y2="146"/>
      <line x1="337" y1="180" x2="351" y2="172"/>
      <line x1="345" y1="208" x2="361" y2="208"/>
      <line x1="337" y1="236" x2="351" y2="244"/>
      <line x1="317" y1="256" x2="325" y2="270"/>
      <line x1="289" y1="264" x2="289" y2="280"/>
      <line x1="261" y1="256" x2="253" y2="270"/>
      <line x1="241" y1="236" x2="227" y2="244"/>
      <line x1="233" y1="208" x2="217" y2="208"/>
      <line x1="241" y1="180" x2="227" y2="172"/>
      <line x1="261" y1="160" x2="253" y2="146"/>
    </g>
  </svg>
  <div class="person" role="img" aria-label="Customer icon"></div>
  <div class="block" style="left:57px;top:138px"><p class="subtitle">subtitle ipsum dolor sit amet</p><h2 class="title">Title lorem ipsum</h2></div>
  <div class="block" style="left:370px;top:141px"><p class="subtitle">subtitle ipsum dolor sit amet</p><h2 class="title">Title lorem ipsum</h2></div>
  <div class="block" style="left:67px;top:278px"><p class="subtitle">subtitle ipsum dolor sit amet</p><h2 class="title">Title lorem ipsum</h2></div>
  <div class="block" style="left:370px;top:276px"><p class="subtitle">subtitle ipsum dolor sit amet</p><h2 class="title">Title lorem ipsum</h2></div>
  <span class="page-num" style="left:8px">9</span>
  <div class="brand footer-brand"><span class="brand__dot"></span>SwiftRelay.net</div>
</section>

</body>
</html>
```